Visual Print Advert for Hair & Makeup Artist

One page colour visual advertisement required for a hair and makeup artist business using pictures and logo with brief description and contact details. MUST have plain white background. All information will be provided I just need someone to put it in a good layout.
Professional, clean and appealing to the eye. Don't want it to look over crowded or busy.
Layout should feature 2-7 photos, without making the page look too busy. Can use any of the photos provided and you are welcome to crop them to change the orientation of the photo.
Content and typeface should fit in with logo and be modern but appeal to the female target audience of brides in Australia aged 22-40yo.
Advertisement is be be used in a bridal magazine and other print media for business advertising purposes.
Updates

Target Market(s)

Future brides in Australia aged 22 - 40yo - females only

Industry/Entity Type

Business

Colors
e34197
ffffff
eda3c7

Requirements
Must have
• White background
Should not have
• NO script writing as it doesn't fit with the logo.

```html
<!DOCTYPE html>
<html lang="en">
<head>
<meta charset="utf-8">
<title>Lumelle Makeup Artistry – Advertisement</title>
<link rel="stylesheet" href="https://fonts.googleapis.com/css2?family=Montserrat:wght@300;700&family=Questrial&display=swap">
<style>
  :root {
    --pink: #e34197;
    --pink-soft: #eda3c7;
    --white: #ffffff;
    --ink: #3a3a3c;
    --ink-soft: #4a4a4c;
    --frame: #8a8a8a;
  }
  * { margin: 0; padding: 0; box-sizing: border-box; }
  html, body {
    width: 845px; height: 1200px; overflow: hidden;
    background: var(--white);
  }
  .advert {
    position: relative; width: 845px; height: 1200px;
    background: var(--white); color: var(--ink);
    font-family: "Questrial", sans-serif;
  }
  .brand {
    position: absolute; top: 58px; left: 0; width: 100%;
    text-align: center;
  }
  .brand-name {
    font-family: "Montserrat", sans-serif; font-weight: 300;
    font-size: 78px; letter-spacing: 18px; line-height: 1;
    color: var(--ink); padding-left: 18px;
  }
  .brand-tagline {
    position: absolute; top: 95px; right: 132px;
    font-size: 21px; letter-spacing: 4px; color: var(--ink);
  }
  .gallery-frame {
    position: absolute; width: 288px; height: 288px;
    border: 1.3px solid var(--frame); border-radius: 34px;
    background: var(--white);
  }
  .frame-tl { left: 121px; top: 221px; }
  .frame-tr { left: 436px; top: 221px; }
  .frame-bl { left: 121px; top: 547px; }
  .frame-br { left: 436px; top: 547px; }
  .gallery-photo {
    position: absolute; left: 28px; top: 26px;
    width: 232px; height: 234px; border-radius: 22px;
  }
  .photo-bride-veil { background: linear-gradient(160deg, #d9d3dc 0%, #8f7f86 45%, #3a2e31 100%); }
  .photo-bride-car { background: linear-gradient(180deg, #6f8a4a 0%, #e9e6df 40%, #d8d4cc 62%, #b4262a 100%); }
  .photo-bride-garden { background: linear-gradient(160deg, #3d5a2a 0%, #7d8f4f 45%, #e6e0d6 80%, #c7b39a 100%); }
  .photo-bridal-party { background: linear-gradient(180deg, #9a9895 0%, #d8c2b0 40%, #2a2b30 75%, #18191c 100%); }
  .divider-mark {
    position: absolute; left: 404px; top: 513px;
    width: 36px; height: 36px; border-radius: 50%;
    background: var(--pink);
  }
  .headline {
    position: absolute; top: 870px; left: 0; width: 100%;
    text-align: center; text-transform: uppercase;
    font-size: 25px; line-height: 33px; color: var(--ink-soft);
  }
  .headline-accent {
    display: block; margin-top: 4px;
    font-family: "Montserrat", sans-serif; font-weight: 700;
    font-size: 37px; line-height: 44px; color: var(--pink);
  }
  .intro {
    position: absolute; top: 1006px; left: 0; width: 100%;
    text-align: center; font-size: 21px; line-height: 28px; color: var(--ink);
  }
  .contact-line {
    position: absolute; top: 1094px; left: 0; width: 100%;
    text-align: center; font-size: 19px; letter-spacing: 0.5px; color: var(--ink);
  }
  .phone-row {
    position: absolute; top: 1120px; left: 121px; width: 603px;
    display: flex; align-items: center; gap: 12px;
  }
  .phone-rule { flex: 1; height: 1.3px; background: var(--ink); }
  .phone-number {
    font-family: "Montserrat", sans-serif; font-weight: 700;
    font-size: 32px; letter-spacing: 1px; color: var(--ink);
  }
</style>
</head>
<body>
<main class="advert">
  <header class="brand">
    <div class="brand-name">LUMELLE</div>
    <div class="brand-tagline">MAKEUP ARTISTRY</div>
  </header>

  <div class="gallery-frame frame-tl">
    <div class="gallery-photo photo-bride-veil" role="img" aria-label="Portrait of a bride with dark hair and a lace veil"></div>
  </div>
  <div class="gallery-frame frame-tr">
    <div class="gallery-photo photo-bride-car" role="img" aria-label="Smiling bride leaning out of a white and red vintage car window"></div>
  </div>
  <div class="gallery-frame frame-bl">
    <div class="gallery-photo photo-bride-garden" role="img" aria-label="Bride holding a bouquet in a leafy garden"></div>
  </div>
  <div class="gallery-frame frame-br">
    <div class="gallery-photo photo-bridal-party" role="img" aria-label="Bride with three bridesmaids in dark dresses"></div>
  </div>

  <div class="divider-mark" role="img" aria-label="Small pink flower accent"></div>

  <h1 class="headline">
    Professionally trained and certified<br>
    mobile hair &amp; makeup artists with over
    <span class="headline-accent">10 Years Experience</span>
  </h1>

  <p class="intro">
    We specialise in naturally enhancing your beauty to have<br>
    you looking and feeling your best on your special day.
  </p>

  <p class="contact-line">mia@lumellemakeup.com.au &nbsp;|&nbsp; www.lumellemakeup.com.au</p>

  <div class="phone-row">
    <span class="phone-rule"></span>
    <span class="phone-number">0400 517 239</span>
    <span class="phone-rule"></span>
  </div>
</main>
</body>
</html>
```